依頼詳細
ラベルデザインの制作
今後様々なフレーバーを展開する予定ですので、応用ができるデザインで
お願い致します。
記載項目
サイズ100(タテ)×70(ヨコ)m/m (±10m/mはOKです)
記載項目:品名「ぽりぽりチップ」、「国産米100%使用」、
あと、いいイメージのコピーがあれば入れたいと思います。
形状は四角、楕円、変形(特にこだわりはありません)
希望イメージ
シンプル 複雑
単色 カラフル
暗い 明るい
日常 高級
遊び心 厳粛
未来的 伝統的
女性的 男性的
希望する色
赤系、黄・オレンジ系、緑系
納品ファイル
• 高解像度JPG (.jpg)
• イラストレーター形式 (.ai)
補足説明
■ 選んだ理由

商品特徴にぴったりで、文字とイラストのかわいさ、色合いや形状などとても良かったと思います。

■ 提案者全員のお礼・コメント

この度ワークルの皆様から多くのご提案を頂き感謝申し上げます。
貴重なお時間を掛けて制作して頂いたデザインですが、
ひとつしか選ぶことが出来ないことを申し訳なく思います。
改めてご提案を頂き有り難う御座いました。
また、ご依頼させて頂く機会があると思います。
その時は是非よろしくお願い致します。

```html
<!DOCTYPE html>
<html lang="ja">
<head>
<meta charset="utf-8">
<title>ぽりぽりチップ えび塩味 ラベル</title>
<link rel="stylesheet" href="https://fonts.googleapis.com/css2?family=Yusei+Magic&family=M+PLUS+Rounded+1c:wght@800&family=Zen+Maru+Gothic:wght@700&display=swap">
<style>
  :root {
    --paper: #ffffff;
    --orange: #e9782a;
    --orange-deep: #d9621c;
    --orange-light: #f08a38;
    --grain: #fbfaf6;
    --brown: #4b2a17;
    --green: #2f9b42;
    --yellow: #f7d81c;
    --red: #d8322a;
    --shrimp-a: #f2a08f;
    --shrimp-b: #d9362c;
  }
  * { margin: 0; padding: 0; box-sizing: border-box; }
  html, body {
    width: 861px; height: 1200px; overflow: hidden; background: var(--paper);
  }
  .label {
    position: relative; width: 861px; height: 1200px;
  }
  .label-body {
    position: absolute; left: 14px; top: 14px; width: 833px; height: 1172px;
    border-radius: 72px;
    background:
      repeating-linear-gradient(172deg,
        var(--orange) 0 48px,
        var(--orange-deep) 48px 70px,
        var(--orange-light) 70px 104px,
        var(--orange-deep) 104px 124px);
    overflow: hidden;
  }
  .grain { position: absolute; left: 0; top: 0; }
  .origin-badge {
    position: absolute; left: 108px; top: 112px; width: 72px; height: 320px;
    background: var(--green); border-radius: 12px;
    color: var(--paper);
    font-family: "Zen Maru Gothic", sans-serif; font-weight: 700; font-size: 38px;
    writing-mode: vertical-rl; text-orientation: upright;
    display: flex; align-items: center; justify-content: center; letter-spacing: 1px;
  }
  .origin-badge .num { text-combine-upright: all; }
  .tagline {
    position: absolute; left: 600px; top: 80px;
    font-family: "M PLUS Rounded 1c", sans-serif; font-weight: 800; font-size: 62px;
    color: var(--yellow); -webkit-text-stroke: 3px var(--red); paint-order: stroke fill;
    transform: rotate(14deg); transform-origin: left top; letter-spacing: -2px;
  }
  .tagline small { font-size: 40px; }
  .tagline-sub {
    position: absolute; left: 700px; top: 240px;
    font-family: "Zen Maru Gothic", sans-serif; font-weight: 700; font-size: 30px;
    color: var(--brown); transform: rotate(28deg); transform-origin: left top;
  }
  .product-name { font-family: "Yusei Magic", sans-serif; color: var(--brown); position: absolute; line-height: 1; }
  .name-top { left: 292px; top: 250px; font-size: 190px; letter-spacing: -6px; }
  .name-chip { left: 300px; top: 530px; font-size: 125px; letter-spacing: -6px; }
  .name-side { left: 610px; top: 590px; font-size: 150px; writing-mode: vertical-rl; letter-spacing: -4px; }
  .shrimp-art {
    position: absolute; left: 115px; top: 740px; width: 235px; height: 200px;
    border-radius: 50% 45% 50% 40%;
    background: radial-gradient(ellipse at 45% 45%, var(--shrimp-a), var(--shrimp-b));
  }
  .flavor {
    position: absolute; left: 0; width: 100%; top: 1048px; text-align: center;
    font-family: "Zen Maru Gothic", sans-serif; font-weight: 700; font-size: 46px;
    color: var(--brown); letter-spacing: 6px; padding-left: 40px;
  }
</style>
</head>
<body>
  <div class="label">
    <div class="label-body"></div>
    <svg class="grain" width="861" height="1200" viewBox="0 0 861 1200" aria-hidden="true">
      <path d="M470,90 C625,82 745,270 758,560 C772,860 680,1135 480,1145 C280,1155 198,900 208,620 C218,300 325,96 470,90 Z" fill="var(--grain)"/>
    </svg>
    <div class="origin-badge">国産米<span class="num">100</span>%使用</div>
    <div class="tagline">さっ<small>く</small>さ<small>く</small></div>
    <div class="tagline-sub">の歯ごたえ</div>
    <div class="product-name name-top">ぽり</div>
    <div class="product-name name-chip">チップ</div>
    <div class="product-name name-side">ぽり</div>
    <div class="shrimp-art" role="img" aria-label="赤いえびのイラスト"></div>
    <div class="flavor">えび塩味</div>
  </div>
</body>
</html>
```